Walk Beside The River

Business Card design

Target Market(s)

People who require support in the commnity

Industry/Entity Type

Mental Health Support

Contact Information for Business Card

Mental Health Support Rosalind Tavener walkbesidetheriver@mailbrook.com.au 0458 906 312 PO Box 627 Maroochydore QLD 4558

Colors
6B429C
8869AF
B7A5CE
E3DAEB
F3F0F8

Requirements
Must have
• Logo & details listed above
Should not have
• No red or orange

```html
<!DOCTYPE html>
<html lang="en">
<head>
<meta charset="utf-8">
<title>Walk Beside The River – Business Card</title>
<link href="https://fonts.googleapis.com/css2?family=Arimo:ital,wght@0,400;0,700;1,400;1,700&display=swap" rel="stylesheet">
<style>
  :root {
    --purple: #6b429c;
    --purple-mid: #8869af;
    --lilac: #b7a5ce;
    --mist: #e3daeb;
    --paper: #fbfaf7;
    --ink-grey: #6f6f6f;
    --rule-grey: #8a8a8a;
    --edge: #c9c22a;
    --backdrop: #1b1b1d;
  }
  * { box-sizing: border-box; margin: 0; padding: 0; }
  html, body {
    width: 1200px; height: 963px; overflow: hidden;
    background: var(--backdrop);
    font-family: "Arimo", Arial, sans-serif;
  }
  .sheet {
    width: 1200px; height: 963px;
    display: flex; flex-direction: column;
    align-items: center; justify-content: center;
    gap: 60px;
  }
  .card {
    position: relative;
    width: 600px; height: 343px;
    background: var(--paper);
    border-radius: 18px;
    border-bottom: 3px solid var(--edge);
  }
  .brand {
    color: var(--purple);
    font-weight: 700;
    white-space: nowrap;
  }
  .card--front .brand {
    position: absolute; left: 0; top: 50%;
    width: 292px;
    transform: translateY(-50%);
    text-align: center;
    font-size: 19px;
  }
  .divider {
    position: absolute; left: 292px; top: 92px;
    width: 1px; height: 160px;
    background: var(--rule-grey);
  }
  .details {
    position: absolute; left: 312px; top: 96px;
    font-style: italic;
    color: var(--ink-grey);
    font-size: 13px; line-height: 1.35;
  }
  .person-name {
    color: var(--purple);
    font-weight: 700;
    font-size: 22px; line-height: 1.1;
  }
  .person-role { font-size: 14px; margin-bottom: 8px; }
  .address { margin-bottom: 8px; }
  .contact { display: flex; align-items: center; gap: 7px; }
  .contact svg { flex: none; width: 13px; height: 13px; }
  .card--back { display: flex; align-items: center; justify-content: center; }
  .card--back .brand { font-size: 30px; }
</style>
</head>
<body>
<main class="sheet">
  <section class="card card--front" aria-label="Business card front">
    <div class="brand">Walk Beside The River</div>
    <div class="divider"></div>
    <div class="details">
      <p class="person-name">Rosalind Tavener</p>
      <p class="person-role">Mental Health Support</p>
      <p class="address">PO Box 627<br>Maroochydore QLD 4558</p>
      <p class="contact">
        <svg viewBox="0 0 16 16" aria-hidden="true"><path d="M4 1.5l2.2 3-1.4 1.6c.8 1.8 2.3 3.3 4.1 4.1l1.6-1.4 3 2.2-1.1 2.5C7 13.4 2.6 9 2 2.6z" fill="none" stroke="var(--purple)" stroke-width="1.5" stroke-linejoin="round"/></svg>
        0458 906 312
      </p>
      <p class="contact">
        <svg viewBox="0 0 16 16" aria-hidden="true"><rect x="1.5" y="3.5" width="13" height="9" rx="1" fill="none" stroke="var(--purple)" stroke-width="1.4"/><path d="M2 4.5l6 4.5 6-4.5" fill="none" stroke="var(--purple)" stroke-width="1.4"/></svg>
        walkbesidetheriver@mailbrook.com.au
      </p>
    </div>
  </section>
  <section class="card card--back" aria-label="Business card back">
    <div class="brand">Walk Beside The River</div>
  </section>
</main>
</body>
</html>
```